Tranvik Leasing Corp - Business Card Design

Need a new modern designed business card that is different and stands out to represent my equipment financing company. Tranvik Leasing Corp finances all types of equipment and all types of industries. We like to do equipment financing a different way by putting customers first and want our card to represent that different approach to business. I want a card that some remembers when they receive it so it sticks in their mind and makes that wow impression.

Card should have a black background so the logo stands out. It can be horizontial or vertical or a combination of both.

Front of card information is below that shows the information that would go on my card. That is where I want a different look or design to stand out. The front could be split black/orange colour so the logo could pop on black side and information on orange side with different lettering. Just outside the box thinking on the front of the card. Open to any type of design.

Back of card is below which i I like unless you have a different spin to provide or a different idea that would make the card better as I am open to anything that looks great.

Target Market(s)

Tranvik Leasing Corp deals with business owners in all industries.

Industry/Entity Type

Business

Contact Information for Business Card

Colors

Designer to choose colors to be used in the design.

Requirements
Must have
• Modern
• Different
• Stand Out
• Makes an Impression

```html
<!DOCTYPE html>
<html lang="en">
<head>
<meta charset="utf-8">
<title>Tranvik Leasing Corp – Business Card</title>
<link href="https://fonts.googleapis.com/css2?family=Montserrat:wght@700&family=Open+Sans:wght@400;600&display=swap" rel="stylesheet">
<style>
  :root {
    --stage: #3a3a3a;
    --card-black: #0f0f10;
    --orange: #f07a1a;
    --orange-light: #f39a2a;
    --orange-deep: #e0601e;
    --red: #c8202a;
    --red-deep: #a8161f;
    --white: #f4f4f4;
    --rule: #c9741f;
    --band-text: #2a1208;
  }
  * { margin: 0; padding: 0; box-sizing: border-box; }
  html, body { width: 1200px; height: 900px; overflow: hidden; }
  body {
    background: var(--stage);
    font-family: "Open Sans", Arial, sans-serif;
    display: flex;
    align-items: center;
    justify-content: center;
    gap: 60px;
  }
  .card {
    position: relative;
    width: 340px;
    height: 580px;
    background: var(--card-black);
    border-radius: 22px;
    overflow: hidden;
    box-shadow: 0 18px 40px rgba(0,0,0,.45);
  }
  /* Front */
  .front-bands {
    position: absolute;
    inset: 0;
    width: 100%;
    height: 100%;
  }
  .card--front .wordmark {
    position: absolute;
    left: 0; right: 0;
    top: 150px;
    justify-content: center;
  }
  .wordmark {
    display: flex;
    align-items: center;
    gap: 10px;
    color: var(--orange);
    font-family: "Open Sans", Arial, sans-serif;
    font-weight: 600;
    font-size: 21px;
    letter-spacing: .04em;
    text-transform: uppercase;
    white-space: nowrap;
  }
  .wordmark__dot {
    width: 14px; height: 14px;
    border-radius: 50%;
    background: var(--orange);
    flex: none;
  }
  /* Back */
  .card--back {
    display: flex;
    flex-direction: column;
    align-items: center;
    text-align: center;
  }
  .card--back .wordmark { margin-top: 120px; font-size: 20px; }
  .holder__name {
    margin-top: 58px;
    font-family: "Montserrat", Arial, sans-serif;
    font-weight: 700;
    font-size: 17px;
    letter-spacing: .3em;
    color: var(--white);
  }
  .holder__title {
    margin-top: 4px;
    font-family: "Montserrat", Arial, sans-serif;
    font-weight: 700;
    font-size: 8px;
    letter-spacing: .2em;
    color: var(--orange);
  }
  .divider {
    width: 240px;
    height: 1px;
    background: var(--rule);
    margin: 16px 0 22px;
  }
  .contact { list-style: none; }
  .contact__item { margin-bottom: 8px; }
  .contact__label {
    display: block;
    font-size: 7px;
    font-weight: 600;
    letter-spacing: .15em;
    color: var(--orange);
  }
  .contact__value {
    display: block;
    font-size: 14px;
    color: var(--white);
  }
  .social { display: flex; gap: 6px; margin-top: 4px; }
  .social__chip { width: 11px; height: 11px; background: var(--orange); border-radius: 2px; }
  .address-band {
    position: absolute;
    left: 0; right: 0; bottom: 0;
    height: 92px;
    background: linear-gradient(160deg, var(--orange) 0%, var(--orange-deep) 40%, var(--red) 100%);
    display: flex;
    flex-direction: column;
    justify-content: center;
    align-items: center;
    color: var(--band-text);
    font-size: 14px;
    line-height: 1.3;
  }
</style>
</head>
<body>
  <section class="card card--front" aria-label="Card front">
    <svg class="front-bands" viewBox="0 0 340 580" preserveAspectRatio="none" aria-hidden="true">
      <defs>
        <linearGradient id="orangeBand" x1="0" y1="0" x2="1" y2="1">
          <stop offset="0" stop-color="#f39a2a"/>
          <stop offset="1" stop-color="#e0601e"/>
        </linearGradient>
        <linearGradient id="redBand" x1="0" y1="0" x2="1" y2="1">
          <stop offset="0" stop-color="#d42a2a"/>
          <stop offset="1" stop-color="#a8161f"/>
        </linearGradient>
      </defs>
      <polygon points="0,0 110,0 0,80" fill="url(#orangeBand)"/>
      <polygon points="0,330 340,230 340,310 0,410" fill="url(#orangeBand)"/>
      <polygon points="0,470 340,370 340,400 0,500" fill="url(#orangeBand)"/>
      <polygon points="110,580 340,450 340,520 230,580" fill="url(#redBand)"/>
    </svg>
    <div class="wordmark"><span class="wordmark__dot"></span>Tranvik Leasing Corp</div>
  </section>

  <section class="card card--back" aria-label="Card back">
    <div class="wordmark">Tranvik Leasing Corp</div>
    <p class="holder__name">MARA ELDEN</p>
    <p class="holder__title">PRESIDENT</p>
    <div class="divider"></div>
    <ul class="contact">
      <li class="contact__item"><span class="contact__label">PHONE</span><span class="contact__value">403 555 0192</span></li>
      <li class="contact__item"><span class="contact__label">EMAIL</span><span class="contact__value">mara@tranvikleasing.ca</span></li>
      <li class="contact__item"><span class="contact__label">WEB</span><span class="contact__value">www.tranvikleasing.ca</span></li>
    </ul>
    <div class="social"><span class="social__chip"></span><span class="social__chip"></span></div>
    <div class="address-band">
      <span>415, 880 – 9 Avenue NE</span>
      <span>Calgary, AB</span>
    </div>
  </section>
</body>
</html>
```